Travertine Marketing Postcard

We have brought quality pool building materials to our customers since 2000. We want our current customers and prospects to see concisely in a post card that we have premium/select travertine coping and pavers as well in stock at great prices. We can deliver the same quality product and service to them with the travertine as we have with our ceramic swimming pool tile. We want them to know that they can call us for a quote. We want them to know that in addition to pricing that is more than competitive, we are offering special freight rates and get the product to them in two business days.

Reason: I need more time to revise and decide.

Industry/Entity Type

Building

Requirements
Must have
• The quality of the product is premium /select. There are 8 colors and the most popular sizes. Even though the product is coming from GA we are offering special freight rates and in some cases can get the product to their project quicker than the local supplier. Orders received by 2:00PM EST can be shipped same day and received in two days. Outstanding customer service.

```html
<!DOCTYPE html>
<html lang="en">
<head>
<meta charset="utf-8">
<title>Heritage Stone Supply – Travertine Postcard</title>
<link href="https://fonts.googleapis.com/css2?family=Open+Sans:wght@400;700&family=Oswald:wght@500&display=swap" rel="stylesheet">
<style>
  :root {
    --ink: #1d1d1d;
    --accent-red: #e0202a;
    --diamond-red: #b8232b;
    --cream: #f7f3dc;
    --stone-light: #e9e1cf;
    --stone-mid: #d6cbb3;
    --band-peach: #f1cdb7;
    --band-pale: #f8e6da;
    --rule-grey: #b9b9b9;
    --paper: #ffffff;
  }
  * { margin: 0; padding: 0; box-sizing: border-box; }
  html, body { width: 800px; height: 1200px; overflow: hidden; background: var(--paper); }
  body { position: relative; font-family: "Open Sans", Arial, sans-serif; color: var(--ink); }

  .front { position: absolute; left: 25px; top: 15px; width: 745px; height: 577px; border: 1px solid #999; overflow: hidden; }
  .hero-photo { position: absolute; left: 0; top: 0; width: 745px; height: 422px;
    background: linear-gradient(180deg, #c9d3d9 0%, #7d8f6a 22%, #a89780 42%, #7fc4cf 58%, #b7a58a 78%, #9c8366 100%); }
  .brand-band { position: absolute; left: 0; top: 422px; width: 745px; height: 155px;
    background: linear-gradient(90deg, var(--band-peach) 0%, var(--band-pale) 70%, #e6ecef 100%); }
  .brand-mark { position: absolute; left: 62px; top: 48px; display: flex; align-items: center; gap: 10px; }
  .dot { width: 14px; height: 14px; border-radius: 50%; background: var(--ink); flex: none; }
  .brand-name { font-size: 22px; font-weight: 400; letter-spacing: 1.5px; color: var(--ink); }
  .tagline { position: absolute; left: 414px; top: 15px; font-size: 23px; line-height: 34px; color: var(--ink); }
  .front-url { position: absolute; left: 366px; top: 99px; font-size: 22px; letter-spacing: 0.5px; color: var(--ink); }

  .back { position: absolute; left: 25px; top: 607px; width: 745px; height: 580px; background: var(--cream); }
  .stone-panel { position: absolute; left: 0; top: 0; width: 348px; height: 448px;
    background: radial-gradient(ellipse at 40% 60%, var(--stone-light), var(--stone-mid)); }
  .pool-photo { position: absolute; left: 35px; top: 38px; width: 282px; height: 202px; border: 2px solid #fff;
    box-shadow: 2px 3px 4px rgba(0,0,0,.35);
    background: linear-gradient(180deg, #b9c7cf 0%, #4f6b3c 35%, #58d0d6 62%, #c7a78a 100%); }
  .back-brand { position: absolute; left: 60px; top: 310px; display: flex; align-items: center; gap: 10px; }
  .back-brand .dot { width: 12px; height: 12px; }
  .back-brand .brand-name { font-size: 17px; }
  .address { position: absolute; left: 70px; top: 387px; font-weight: 700; font-size: 18px; line-height: 26px; }
  .address svg { position: absolute; left: -19px; top: 6px; }

  .ornament-rule { position: absolute; left: 362px; top: 40px; width: 355px; height: 14px; }
  .features { position: absolute; left: 366px; top: 64px; list-style: none; font-weight: 700; font-size: 19px; line-height: 26px; }
  .features li { position: relative; padding-left: 21px; }
  .features li::before { content: ""; position: absolute; left: 3px; top: 8px; width: 10px; height: 10px;
    border: 2px solid var(--diamond-red); transform: rotate(45deg); }
  .service-banner { position: absolute; left: 371px; top: 372px; width: 332px; height: 80px; }
  .service-text { position: absolute; left: 371px; top: 381px; width: 332px; text-align: center;
    font-family: "Oswald", "Arial Narrow", sans-serif; font-weight: 500; font-size: 24px; line-height: 29px; color: #fff; }

  .contact-web { position: absolute; left: 52px; top: 500px; font-weight: 700; font-size: 19px; line-height: 24px; }
  .contact-web div { position: relative; padding-left: 40px; }
  .contact-web svg { position: absolute; left: 0; top: 5px; }
  .contact-phone { position: absolute; left: 410px; top: 475px; font-weight: 700; font-size: 19px; line-height: 24px; }
  .contact-phone div { position: relative; padding-left: 38px; }
  .contact-phone svg { position: absolute; left: 0; top: 4px; }
</style>
</head>
<body>
  <section class="front">
    <div class="hero-photo" role="img" aria-label="Backyard swimming pool with travertine coping, raised spa and stone pergola"></div>
    <div class="brand-band">
      <div class="brand-mark"><span class="dot"></span><span class="brand-name">HERITAGE STONE SUPPLY</span></div>
      <p class="tagline">Your Source For Quality<br>Pool Building Materials</p>
      <p class="front-url">WWW.HERITAGEPOOLSTONE.COM</p>
    </div>
  </section>

  <section class="back">
    <div class="stone-panel" role="img" aria-label="Travertine stone texture background">
      <div class="pool-photo" role="img" aria-label="Freeform backyard pool with tile border and brick coping"></div>
    </div>
    <div class="back-brand"><span class="dot"></span><span class="brand-name">HERITAGE STONE SUPPLY</span></div>
    <p class="address">
      <svg width="14" height="14" viewBox="0 0 14 14"><path d="M1 1 L13 4 L8 6 L7 13 Z" fill="none" stroke="var(--diamond-red)" stroke-width="1.6"/></svg>
      4120 Meadow Ridge Ct<br>Lilburn, GA 30047
    </p>

    <svg class="ornament-rule" viewBox="0 0 355 14">
      <line x1="0" y1="7" x2="355" y2="7" stroke="var(--rule-grey)" stroke-width="3"/>
      <circle cx="178" cy="7" r="5" fill="var(--rule-grey)"/>
    </svg>
    <ul class="features">
      <li>Premium/Select Travertine<br>Coping &amp; Pavers In Stock</li>
      <li>8 Colors Of Most Popular<br>Sizes To Choose From</li>
      <li>Special Freight Rates</li>
      <li>Super fast Delivery</li>
      <li>Orders Received by 2:00 PM EST<br>can be shipped same day and<br>received in two days</li>
      <li>Call Us Today For A Quote</li>
    </ul>

    <svg class="service-banner" viewBox="0 0 332 80">
      <polygon fill="var(--accent-red)" points="0,0 332,0 322,10 332,20 322,30 332,40 322,50 332,60 322,70 332,80 0,80 10,70 0,60 10,50 0,40 10,30 0,20 10,10"/>
    </svg>
    <p class="service-text">OUTSTANDING<br>CUSTOMER SERVICE</p>

    <div class="contact-web">
      <div><svg width="16" height="16" viewBox="0 0 16 16"><circle cx="8" cy="8" r="6" fill="none" stroke="var(--diamond-red)" stroke-width="2"/><line x1="2" y1="8" x2="14" y2="8" stroke="var(--diamond-red)" stroke-width="1.2"/><line x1="8" y1="2" x2="8" y2="14" stroke="var(--diamond-red)" stroke-width="1.2"/></svg>www.heritagepoolstone.com</div>
      <div><svg width="20" height="14" viewBox="0 0 20 14"><rect x="1" y="1" width="18" height="12" fill="none" stroke="var(--diamond-red)" stroke-width="1.3"/><path d="M1 1 L10 8 L19 1" fill="none" stroke="var(--diamond-red)" stroke-width="1.3"/></svg>info@heritagepoolstone.com</div>
    </div>

    <div class="contact-phone">
      <div><svg width="18" height="14" viewBox="0 0 18 14"><path d="M1 5 Q9 -1 17 5 L14 7 L12 4 L6 4 L4 7 Z" fill="var(--diamond-red)"/><rect x="4" y="7" width="10" height="6" fill="var(--diamond-red)"/></svg>555.210.4400</div>
      <div><svg width="18" height="18" viewBox="0 0 18 18"><circle cx="9" cy="9" r="8" fill="none" stroke="var(--diamond-red)" stroke-width="1.3"/><path d="M6 5 Q5 10 11 13 L12 11 L10 10 L8 8 L9 6 Z" fill="var(--diamond-red)"/></svg>Toll Free: 800.555.0142</div>
      <div><svg width="18" height="16" viewBox="0 0 18 16"><rect x="4" y="1" width="10" height="6" fill="none" stroke="var(--diamond-red)" stroke-width="1.3"/><rect x="1" y="7" width="16" height="8" fill="var(--diamond-red)"/></svg>555.210.4411</div>
    </div>
  </section>
</body>
</html>
```